Tallwater Builders Guild Membership

UPDATED files - 06/03/2021
Digital brochure needed for construction contractor related nonprofit organization.
Document will be primarily for digital viewing with potential for print version. Should be branded with our branding (logo attached). This is intended to be a multiple page document, plan to print and web (email) use. Standard Letter size document 8.5 x 11 inch
Portrait format preferred
The attached project brief includes a cover, 4 internal pages, and a back cover. This is flexible pending design layout
Target Market(s)
Residential construction business owners
Requirements
Must have
- See attached brief.Orange color palette: RGB: (253,153,0)
Nice to have
- See attached bief
Should not have
- No suit or ties. button up shirt okay, but not white collar worker.

```html
<!DOCTYPE html>
<html lang="en">
<head>
<meta charset="utf-8">
<title>Tallwater Builders Guild – Membership Brochure</title>
<link href="https://fonts.googleapis.com/css2?family=Oswald:wght@400;500&family=Open+Sans:wght@400;600;700&family=Montserrat:wght@800&display=swap" rel="stylesheet">
<style>
:root{
  --orange:#fd9900;
  --orange-deep:#f08c00;
  --charcoal:#2d2d30;
  --charcoal-2:#3a3a3d;
  --ink:#333;
  --paper:#fff;
  --backdrop:#d9dadb;
  --muted:#555;
}
*{margin:0;padding:0;box-sizing:border-box}
html,body{width:1200px;height:2189px;overflow:hidden;background:var(--backdrop)}
body{position:relative;font-family:"Open Sans",sans-serif;color:var(--ink)}
.page{position:absolute;width:500px;height:646px;background:var(--paper);overflow:hidden;box-shadow:4px 5px 10px rgba(0,0,0,.28)}
.p1{left:88px;top:75px}.p2{left:610px;top:75px}
.p3{left:88px;top:745px}.p4{left:610px;top:745px}
.p5{left:88px;top:1416px}.p6{left:610px;top:1416px}
.abs{position:absolute}
.photo{position:absolute}
.wordmark{font-family:"Montserrat",sans-serif;font-weight:800;color:var(--charcoal);text-align:center;line-height:1.05;letter-spacing:-.5px}
.heading{font-family:"Oswald",sans-serif;font-weight:400;color:var(--orange);font-size:14px;letter-spacing:.2px;text-transform:uppercase}
.body{font-size:7px;line-height:1.5;color:var(--muted)}
.body p+p{margin-top:7px}
.dark{background:var(--charcoal)}
.dark .body,.on-dark{color:#e4e4e4}
.on-orange{color:#fff}
.tab{position:absolute;font-family:"Oswald",sans-serif;color:#fff;font-size:13px;padding:0 0 0 15px;line-height:26px}
ul.cols{list-style:none;display:grid;grid-template-columns:repeat(3,1fr);gap:2px 10px;font-size:7px;color:var(--muted)}
ul.cols li::before{content:"• ";color:var(--orange)}
.value{display:flex;align-items:center;gap:12px;height:34px;font-size:10px;color:var(--charcoal);text-transform:uppercase}
.hex{width:24px;height:24px;flex:none}
.feature{display:flex;gap:8px;align-items:center;font-size:7px;color:var(--muted);margin-bottom:9px}
.feature svg,.policy svg{flex:none}
.policy{display:flex;gap:14px;align-items:center;font-size:7.5px;line-height:1.45;color:var(--muted);margin-bottom:14px}
.person{position:absolute;left:18px;display:flex;align-items:center;gap:24px}
.portrait{width:78px;height:78px;border-radius:50%;background:linear-gradient(#c9c2b8,#8d8478);border:2px solid #fff}
.person h4{font-family:"Open Sans",sans-serif;font-weight:700;font-size:11.5px;color:var(--charcoal)}
.person p{font-size:7.5px;color:var(--charcoal);line-height:1.3}
</style>
</head>
<body>

<!-- Cover -->
<section class="page p1">
  <div class="wordmark abs" style="left:0;right:0;top:30px;font-size:30px">TALLWATER<br>BUILDERS GUILD</div>
  <svg class="abs" style="left:0;top:113px" width="500" height="12"><polygon points="0,0 265,0 253,12 0,12" fill="var(--orange)"/></svg>
  <div class="photo" role="img" aria-label="Smiling young construction worker in a white hard hat and safety vest carrying lumber on his shoulder" style="left:0;top:127px;width:500px;height:346px;background:linear-gradient(135deg,#c9cdd2,#b06a4a 45%,#8a9aa8)"></div>
  <svg class="abs" style="left:0;top:473px" width="500" height="12"><polygon points="250,0 500,0 500,12 238,12" fill="var(--orange)"/></svg>
  <h1 class="abs" style="left:0;right:0;top:490px;text-align:center;font-family:Oswald,sans-serif;font-weight:500;font-size:25px;line-height:34px;color:var(--charcoal)">HELPING YOU REDUCE RISKS AND INJURIES<br>WHILE IMPROVING PROFITABILITY</h1>
  <div class="abs" style="left:52px;right:58px;top:565px;border-top:1px solid #999"></div>
  <p class="abs" style="left:0;right:0;top:572px;text-align:center;font-size:9.5px;color:var(--orange)">NONPROFIT ORGANIZATION SERVING THE CONSTRUCTION INDUSTRY</p>
  <div class="abs dark" style="left:0;bottom:0;width:500px;height:30px;display:flex;align-items:center;justify-content:center;gap:5px;font-size:9.5px;color:var(--orange)">
    <svg width="10" height="10" viewBox="0 0 10 10"><circle cx="5" cy="5" r="4.2" fill="none" stroke="var(--orange)"/><path d="M1 5h8M5 1c-2 2.5-2 5.5 0 8M5 1c2 2.5 2 5.5 0 8" fill="none" stroke="var(--orange)" stroke-width=".8"/></svg>
    tallwaterguild.org
  </div>
</section>

<!-- About -->
<section class="page p2">
  <div class="abs dark" style="left:0;top:0;width:500px;height:208px"></div>
  <svg class="abs" style="left:0;top:0" width="215" height="36"><polygon points="0,0 215,0 200,36 0,36" fill="var(--orange)"/></svg>
  <div class="tab" style="top:4px;font-size:12px">ABOUT US</div>
  <div class="abs body on-dark" style="left:15px;top:50px;width:470px">
    <p><b>TBG</b> is organized as a 501c6 membership organization supported by a 501c3 charitable foundation. Our foundation allows us to provide access to training and education resources to an underserved community of contractors, supporting them in developing a sustainable and profitable business.</p>
    <p>We invite you to join a community of contractors who are better prepared to overcome challenges within the industry, empowering them to share ideas, lessons learned, proven practices, and insights with other industry leaders.</p>
  </div>
  <div class="abs body on-dark" style="left:15px;top:138px;width:228px;text-align:justify"><b style="color:var(--orange)">MISION</b><br>To promote, educate and advance a diverse contractor community by providing pathways of accessibility to help build a stronger foundation for a better future.</div>
  <div class="abs body on-dark" style="left:255px;top:137px;width:228px;text-align:justify"><b style="color:var(--orange)">VISION</b><br>To become the preferred organization for construction contractors striving to be the best in their trade through education, training, and ongoing development.</div>
  <div class="photo" role="img" aria-label="Contractors studying course materials at a classroom table" style="left:15px;top:223px;width:228px;height:124px;background:linear-gradient(135deg,#9a8f80,#6a655e)"></div>
  <div class="photo" role="img" aria-label="Team of workers in hard hats and vests reviewing a laptop on site" style="left:254px;top:223px;width:229px;height:124px;background:linear-gradient(135deg,#b7b08a,#7b8a6a)"></div>
  <div class="heading abs" style="left:15px;top:366px">CORE VALUES</div>
  <div class="abs" style="left:15px;top:386px;width:470px">
    <div class="value"><svg class="hex" viewBox="0 0 24 24"><polygon points="12,1 22,6.5 22,17.5 12,23 2,17.5 2,6.5" fill="var(--orange)"/><circle cx="12" cy="10" r="3.5" fill="var(--charcoal)"/><rect x="7" y="14" width="10" height="5" fill="var(--charcoal)"/></svg>Empower through learning &amp; development</div>
    <div class="value"><svg class="hex" viewBox="0 0 24 24"><polygon points="12,1 22,6.5 22,17.5 12,23 2,17.5 2,6.5" fill="var(--orange)"/><circle cx="10" cy="13" r="4" fill="none" stroke="var(--charcoal)" stroke-width="2"/><circle cx="15" cy="9" r="2.5" fill="var(--charcoal)"/></svg>Strengthen &amp; sustain the industry</div>
    <div class="value"><svg class="hex" viewBox="0 0 24 24"><polygon points="12,1 22,6.5 22,17.5 12,23 2,17.5 2,6.5" fill="var(--orange)"/><circle cx="10" cy="9" r="3" fill="var(--charcoal)"/><rect x="6" y="13" width="9" height="5" fill="var(--charcoal)"/><circle cx="16" cy="14" r="2.5" fill="var(--charcoal)"/></svg>Build partnerships to benefit underserved communities</div>
    <div class="value"><svg class="hex" viewBox="0 0 24 24"><polygon points="12,1 22,6.5 22,17.5 12,23 2,17.5 2,6.5" fill="var(--orange)"/><rect x="6" y="11" width="3" height="7" fill="var(--charcoal)"/><path d="M10 11l3-5h1v4h4v7h-8z" fill="var(--charcoal)"/></svg>Act with integrity, respect, and honesty</div>
    <div class="value"><svg class="hex" viewBox="0 0 24 24"><polygon points="12,1 22,6.5 22,17.5 12,23 2,17.5 2,6.5" fill="var(--orange)"/><path d="M7 10a5 5 0 0110 0z" fill="var(--charcoal)"/><rect x="8" y="11" width="8" height="7" fill="var(--charcoal)"/></svg>Promote diversity, equity, and inclusion throughout the industry</div>
  </div>
  <div class="abs" style="left:0;top:580px;width:500px;height:66px;background:var(--orange)"></div>
  <svg class="abs" style="left:0;top:580px" width="215" height="22"><polygon points="0,0 215,0 203,22 0,22" fill="var(--charcoal)"/></svg>
  <div class="tab" style="top:578px;font-size:11.5px">DIVERSITY, EQUITY &amp; INCLUSION</div>
  <p class="abs body on-orange" style="left:15px;top:610px;width:470px">TBG promotes and encourages open dialogue and positive working environments for BIPOC and other identity groups, to thrive within a contractor community and facilitate a more inclusive and resilient future.</p>
</section>

<!-- Technical assistance / safety -->
<section class="page p3">
  <div class="photo" role="img" aria-label="Worker in a blue hard hat and orange vest operating machinery at an industrial site" style="left:0;top:0;width:500px;height:207px;background:linear-gradient(120deg,#4a4f55,#d07a3a 50%,#2e4c6e)"></div>
  <svg class="abs" style="left:0;top:0" width="45" height="207"><polygon points="0,0 40,0 0,207" fill="var(--charcoal)"/><polyline points="42,0 3,207" stroke="var(--orange)" stroke-width="3" fill="none"/></svg>
  <div class="heading abs" style="left:21px;top:224px">TECHNICAL ASSISTANCE</div>
  <div class="abs body" style="left:21px;top:243px;width:465px;text-align:justify">
    <p>One of our primary goals is to provide technical assistance to the contractor community based on individual level of competency. We understand that the needs of contractors vary greatly based on experience, training, past mentorship. Technical assistance takes many forms including business formation assistance, contractor licensing (OR, WA), insurance consulting, access to legal resources as well as assistance with government program funding (PPP Loans, business grants, scholarships), and various networking opportunities.</p>
    <p>We also provide technical assistance in one-on-one setting as well as business workshops and ongoing assistance. Additionally, we offer assistance with COBID initial and renewal applications.</p>
  </div>
  <div class="abs dark" style="left:0;top:347px;width:500px;height:150px"></div>
  <div class="photo" role="img" aria-label="Smiling office team reviewing a laptop together" style="left:252px;top:347px;width:248px;height:150px;background:linear-gradient(135deg,#eef0f2,#c9ccd0);clip-path:polygon(15px 0,100% 0,100% 100%,0 100%)"></div>
  <div class="abs" style="left:277px;top:358px;display:flex;align-items:center;gap:5px;font-size:14px;color:#555"><span style="width:11px;height:11px;border-radius:50%;background:var(--orange);display:inline-block"></span>SafeLedger</div>
  <div class="heading abs" style="left:23px;top:355px">SAFETY &amp; COMPLIANCE</div>
  <div class="abs body on-dark" style="left:23px;top:375px;width:215px;text-align:justify;font-size:6.6px">
    <p><b>SafeLedger.com</b> is a secure, web-based application that enables employers to create each state's first report of injury, track injuries, and view injury metrics in real-time. The software includes the ability automatically generate and download PDF versions of OSHA forms 301, 300, and 300A to print, share, or email.</p>
    <p>Works with all devices: computers, tablets, and smartphones. Once data is entered and intuitively updated on all other forms, SafeLedger will automatically generate benchmark figures with no additional input by location and log.</p>
  </div>
  <div class="heading abs" style="left:21px;top:507px">SITESURE SAFETY</div>
  <div class="abs body" style="left:21px;top:527px;width:215px;text-align:justify;font-size:6.6px">
    <p>Our partnership with SiteSure gives you the tools you need to protect your workers, meet compliance requirements, and create a positive workspace environment for your employees and others you may work with.</p>
    <p>SiteSure's staff of safety professionals, safety trainers, and administrative staff combined with innovative technology has helped thousands of contractors across the nation save money and improve efficiency.</p>
  </div>
  <p class="abs" style="left:260px;top:510px;font-size:6.8px;color:var(--orange)">Included in the mobile app are the following:</p>
  <div class="abs" style="left:260px;top:524px;width:230px">
    <div class="feature"><svg width="18" height="18" viewBox="0 0 18 18"><rect x="3" y="2" width="12" height="14" fill="none" stroke="var(--orange)" stroke-width="1.3"/><path d="M6 6h6M6 9h6M6 12h4" stroke="var(--orange)"/></svg>Over 1,200 bilingual (Spanish/English) safety lessons with digital signoff rosters</div>
    <div class="feature"><svg width="18" height="18" viewBox="0 0 18 18"><rect x="2" y="4" width="14" height="11" fill="none" stroke="var(--orange)" stroke-width="1.3"/><path d="M5 8h8M5 11h5" stroke="var(--orange)"/></svg>An online form builder to create job and equipment-specific inspection forms</div>
    <div class="feature"><svg width="18" height="18" viewBox="0 0 18 18"><circle cx="9" cy="9" r="6.5" fill="none" stroke="var(--orange)" stroke-width="1.3"/><path d="M6 9l2 2 4-4" stroke="var(--orange)" fill="none"/></svg>Mobile-accessible document storage repository</div>
    <div class="feature"><svg width="18" height="18" viewBox="0 0 18 18"><rect x="2" y="3" width="14" height="9" fill="none" stroke="var(--orange)" stroke-width="1.3"/><path d="M9 12v3M6 16h6" stroke="var(--orange)"/></svg>Live monthly webinars addressing safety topics</div>
  </div>
  <svg class="abs" style="left:0;top:634px" width="500" height="12"><polygon points="245,0 500,0 500,12 240,12" fill="var(--orange)"/></svg>
</section>

<!-- Education -->
<section class="page p4">
  <div class="photo" role="img" aria-label="Group of diverse construction workers in hard hats giving a joint high five" style="left:0;top:0;width:500px;height:207px;background:linear-gradient(160deg,#b9d3ea,#e0c48a 55%,#4c6e9a)"></div>
  <svg class="abs" style="left:0;top:207px" width="500" height="12"><polygon points="238,0 500,0 500,12 250,12" fill="var(--orange)"/></svg>
  <div class="heading abs" style="left:15px;top:233px">CONTRACTOR EDUCATION</div>
  <div class="abs body" style="left:15px;top:256px;width:470px">
    <p>We provide education through live classes, training workshops, and via eLearning courses. We provide in-class training for EPA/RRP Certification, CPR/First Aid certification, Fall Protection certification, and the Oregon CCB 16-hour Pre-licensing training.</p>
    <p>We also offer a full suite of online construction education courses to help contractors learn at their own pace and convenience. Courses are mobile-friendly and available in English or Spanish. Our online course catalog includes</p>
  </div>
  <ul class="cols abs" style="left:15px;top:324px;width:470px">
    <li>OSHA 10 &amp; 30 training</li><li>Administrative courses</li><li>Environmental exposure</li>
    <li>Trade-specific skills</li><li>HAZWOPER</li><li>And much more…</li>
    <li>Safety courses</li><li>Construction management</li><li></li>
  </ul>
  <p class="abs body" style="left:15px;top:375px;width:470px">We also offer targeted training tracks in specific skillsets to promote business development necessary to operate an efficient business. Skillsets include:</p>
  <ul class="cols abs" style="left:15px;top:408px;width:470px">
    <li>Business operations</li><li>Understanding financials</li><li>Marketing &amp; Networking</li>
    <li>Business Law &amp; Contracts</li><li>Safety &amp; Compliance training</li><li>Business Management / HR</li>
  </ul>
  <div class="abs dark" style="left:0;top:455px;width:500px;height:191px"></div>
  <div class="heading abs" style="left:15px;top:464px">CONTRACTOR EDUCATION</div>
  <div class="abs body on-dark" style="left:15px;top:487px;width:470px">
    <p>BuildFinder.com is a FREE effortless way for contractors to connect with property owners to search for a contractor in their local area. As marketing has evolved, contractors need to adopt a variety of online tools and technologies to help gain more online visibility which will result in more business for you.</p>
    <p>The site gives instant access to residential and commercial contractors, an online bid request system, links to the contractor's social media pages and a review system all in one spot.</p>
    <p>Create your business profile and easily manage your unlimited FREE Bid requests, reviews, social media, photo gallery, video links just to name a few. Having a profile listing adds legitimacy to your business.</p>
    <p>A prime advantage of having your business listed is the SEO and relevant incoming "links to your business". Link building is an important building block of any SEO campaign.</p>
  </div>
</section>

<!-- Membership / policies -->
<section class="page p5">
  <svg class="abs" style="left:0;top:0" width="500" height="22"><polygon points="0,0 500,0 500,8 0,8" fill="#fff"/><polygon points="0,0 300,0 290,22 0,22" fill="var(--orange)"/></svg>
  <div class="abs dark" style="left:0;top:22px;width:500px;height:190px"></div>
  <div class="photo" role="img" aria-label="Worker in a safety vest holding a yellow hard hat beside an excavator" style="left:310px;top:22px;width:190px;height:190px;background:linear-gradient(135deg,#9bb0c4,#e8b623 55%,#c9cf58);clip-path:polygon(60px 0,100% 0,100% 100%,0 100%)"></div>
  <div class="heading abs" style="left:21px;top:60px">MEMBERSHIP LEVELS</div>
  <div class="abs body on-dark" style="left:21px;top:84px;width:310px;font-size:7.5px">
    <p>Stay informed with valuable industry related articles intended to help your businesses be safe and successful. These articles include best practices, news events and expert advice which are researched and developed by our construction industry and safety experts, and compliance specialists.</p>
    <p>You will also be informed with OSHA and EPA regulations and rules that help you stay compliant.</p>
  </div>
  <svg class="abs" style="left:0;top:212px" width="500" height="10"><polygon points="205,0 500,0 500,10 200,10" fill="var(--orange)"/></svg>
  <div class="heading abs" style="left:21px;top:238px">COURSE POLICIES</div>
  <div class="abs" style="left:25px;top:266px;width:455px">
    <div class="policy"><svg width="28" height="24" viewBox="0 0 28 24"><rect x="4" y="4" width="20" height="14" fill="none" stroke="var(--orange)" stroke-width="1.5"/><path d="M1 20h26" stroke="var(--orange)" stroke-width="1.5"/></svg>Preregistration is required for all classes. In order to guarantee a space in the class of your choice, registration with payment should be made at least 1 week in advance of the course. Class space is limited, register early.</div>
    <div class="policy"><svg width="28" height="24" viewBox="0 0 28 24"><circle cx="14" cy="12" r="9" fill="none" stroke="var(--orange)" stroke-width="1.5"/><circle cx="14" cy="10" r="3" fill="var(--orange)"/></svg>Classes with low enrollment (less than 5 students) may be subject to cancellation and/or rescheduling. If Tallwater Builders Guild cancels a class, we will promptly notify you. Every effort will be made to reschedule your training.</div>
    <div class="policy"><svg width="28" height="24" viewBox="0 0 28 24"><rect x="6" y="3" width="16" height="18" fill="none" stroke="var(--orange)" stroke-width="1.5"/><path d="M9 8h10M9 12h10M9 16h6" stroke="var(--orange)"/></svg>Course confirmations will be sent to the e-mail provided at the time of registration.</div>
    <div class="policy"><svg width="28" height="24" viewBox="0 0 28 24"><circle cx="14" cy="13" r="9" fill="none" stroke="var(--orange)" stroke-width="1.5"/><path d="M14 8v5l3 2M11 2h6" stroke="var(--orange)" stroke-width="1.5" fill="none"/></svg>Please arrive on time. Students arriving more than 10 minutes late for any scheduled training will be required to reschedule. Tallwater Builders Guild will not issue refunds for students who are late. Please respect the time of all of our students by arriving 5-10 minutes early.</div>
  </div>
  <div class="abs" style="left:0;top:455px;width:500px;height:191px;background:var(--orange)"></div>
  <div class="abs" style="left:21px;top:462px;font-family:Oswald,sans-serif;font-size:13px;color:var(--charcoal)">CANCELLATION/RESCHEDULE POLICY</div>
  <div class="abs body on-orange" style="left:21px;top:480px;width:225px;font-size:7px">
    <p>Any cancellation for live classes between 21 and 8 days prior to the class are subject to a 50% refund, and all cancellation 7 days or less are non-refundable.</p>
    <p style="margin-top:10px">Students rescheduling is subject to a $75 rescheduling fee regardless of the time frame.</p>
  </div>
  <div class="abs" style="left:23px;top:570px;font-size:7.5px;font-weight:700;color:var(--charcoal)">Tallwater Builders Guild Classroom:</div>
  <div class="abs" style="left:23px;top:587px;font-size:7px;line-height:1.45;color:var(--charcoal)">
    <div style="display:flex;gap:6px"><svg width="7" height="9" viewBox="0 0 7 9"><path d="M3.5 9C1 5.5 0 4.5 0 3.5a3.5 3.5 0 017 0C7 4.5 6 5.5 3.5 9z" fill="var(--charcoal)"/></svg><span>4820 Ridgeline Ave., Suite #210,<br>Cedar Falls, OR 97000</span></div>
    <div style="display:flex;gap:6px;margin-top:3px"><svg width="7" height="8" viewBox="0 0 8 8"><path d="M1 0l2 2-1 1.5a5 5 0 002.5 2.5L6 5l2 2-1.5 1C3 8 0 5 0 1.5z" fill="var(--charcoal)"/></svg>800-555-0147</div>
  </div>
  <div class="photo" role="img" aria-label="Instructor presenting to students in a training classroom" style="left:265px;top:480px;width:213px;height:142px;background:linear-gradient(135deg,#d6d9dd,#7d7f84);border:2px solid #fff"></div>
</section>

<!-- Back cover -->
<section class="page p6">
  <div class="wordmark abs" style="left:0;right:0;top:33px;font-size:27px">TALLWATER<br>BUILDERS GUILD</div>
  <div class="abs" style="left:0;top:128px;width:500px;height:346px;background:var(--orange)"></div>
  <div class="photo" role="img" aria-label="Construction worker in a yellow hard hat hammering framing on a rooftop" style="left:265px;top:128px;width:235px;height:346px;background:linear-gradient(160deg,#bfd3e6,#8a9db0 40%,#7b5a3a);clip-path:polygon(78px 0,100% 0,100% 100%,0 100%)"></div>
  <svg class="abs" style="left:265px;top:128px" width="90" height="346"><polygon points="70,0 86,0 14,346 0,346" fill="var(--charcoal)"/></svg>
  <div class="person" style="top:168px"><div class="portrait" role="img" aria-label="Portrait photo of Dana Whitlock"></div><div><h4>Dana Whitlock</h4><p>Tallwater Builders Guild<br>Director of Safety Education</p></div></div>
  <div class="person" style="top:257px"><div class="portrait" role="img" aria-label="Portrait photo of Evan Marsh"></div><div><h4>Evan Marsh</h4><p>Marketing and Social Media Coordinator at<br>Tallwater Builders Guild, Inc</p></div></div>
  <div class="person" style="top:351px"><div class="portrait" role="img" aria-label="Portrait photo of Owen Reyes"></div><div><h4>Owen Reyes</h4><p>Graphic and Web Designer at<br>Tallwater Builders Guild</p></div></div>
  <div class="wordmark abs" style="left:0;right:0;top:528px;font-size:24px">TALLWATER BUILDERS GUILD</div>
  <p class="abs" style="left:0;right:0;top:574px;text-align:center;font-size:10px;color:var(--charcoal)">4820 Ridgeline Ave., Suite #210, Cedar Falls, OR 97000</p>
  <div class="abs" style="left:0;bottom:0;width:500px;height:30px;background:var(--orange);display:flex;align-items:center;justify-content:space-around;font-size:9.5px;color:var(--charcoal)">
    <span style="display:flex;gap:5px;align-items:center"><svg width="10" height="10" viewBox="0 0 10 10"><circle cx="5" cy="5" r="4.2" fill="none" stroke="var(--charcoal)"/><path d="M1 5h8M5 1c-2 2.5-2 5.5 0 8M5 1c2 2.5 2 5.5 0 8" fill="none" stroke="var(--charcoal)" stroke-width=".8"/></svg>tallwaterguild.org</span>
    <span style="display:flex;gap:5px;align-items:center"><svg width="9" height="9" viewBox="0 0 8 8"><path d="M1 0l2 2-1 1.5a5 5 0 002.5 2.5L6 5l2 2-1.5 1C3 8 0 5 0 1.5z" fill="var(--charcoal)"/></svg>971-555-0182</span>
    <span style="display:flex;gap:5px;align-items:center"><svg width="11" height="8" viewBox="0 0 11 8"><rect x=".5" y=".5" width="10" height="7" fill="var(--charcoal)"/><path d="M.5 .5l5 4 5-4" stroke="var(--orange)" fill="none" stroke-width=".8"/></svg>hello@tallwaterguild.org</span>
  </div>
</section>

</body>
</html>
```